【本のタイトル】
●パート主婦が口ぐせを変えて手作り雑貨の通販サイトを始めて
2年で月商200万円に育てた道のり

※本編を参考資料としてつけます

●読者プレゼントは
文面の中にもありますが、森田恭平先生主催のサンセットベルというトーク公演の時に登壇して私が話した内容の動画を、改めて撮影してユーチューブの限定公開にしたものをプレゼントします。

【デザイナーさんにお願いです】

これは、「絶対こうしてください」ということではないのですが、
「できたら、したい」というお願いです。

本編をお読みいただくとわかりますように、
私の人生が森田恭平先生の著書との出会いによって、
大きく変わり、この本の中にも、森田先生のエッセンスが、
たくさん詰まっています。
また、先生への感謝のサプライズとしての意味合いの出版でもあります。♬(^^♪

ですから、表紙デザインのモチーフとして、

例えばですが、
森田恭平先生の
・教材「ロケットチャレンジワーク」のダイナマイトイラストのモチーフが入っている
・ご著書「迷いの霧の晴らし方」のピンク色に黒ゴシックのタイトル、
プレゼントが黄色の丸、という組み合わせ
※ココでいう迷いの霧の晴らし方は、2006年に発売開始した時はピンク色の表紙でした。昨年同じ内容で表紙が飛び込みするような人の表紙カバーになりましたけど、私のイメージは最初のショッキングピンクの表紙のものです
・「弱気な朝に読む帳」「遠い友へ届ける手紙」のイメージ

など、「あからさまじゃないけど、エッセンス入ってる」
みたいなデザインにしたいと考えています。

本文のモチーフがかわいいイラストで描かれていて惹かれました。

ご提案くださいまして、本当にありがとうございます。皆様の素敵なご提案がたくさんあって迷いました。また次回もよろしくお願いいたします。

```html
<!DOCTYPE html>
<html lang="ja">
<head>
<meta charset="utf-8">
<title>2年で月商200万円に育てた道のり</title>
<link rel="stylesheet" href="https://fonts.googleapis.com/css2?family=Noto+Sans+JP:wght@500;700;900&display=swap">
<style>
  :root {
    --green-deep: #1f7a1c;
    --green-main: #4fb81e;
    --green-light: #a8de1c;
    --lime: #d6ef2a;
    --ink: #111111;
    --white: #ffffff;
    --accent: #ffe600;
  }
  * { margin: 0; padding: 0; box-sizing: border-box; }
  html, body { width: 750px; height: 1200px; overflow: hidden; background: var(--white); }
  body { font-family: "Noto Sans JP", sans-serif; color: var(--ink); }
  .cover { position: relative; width: 750px; height: 1200px; overflow: hidden; background: var(--white); }

  .cover__backdrop {
    position: absolute; left: 0; top: 0; width: 750px; height: 1010px;
    background: radial-gradient(ellipse at 45% 40%, var(--lime) 0%, var(--green-light) 35%, var(--green-main) 70%, var(--green-deep) 100%);
  }

  .lead-band {
    position: absolute; left: 0; top: 0; width: 750px; height: 62px;
    background: var(--green-deep);
    display: flex; align-items: center; justify-content: center;
  }
  .lead-band__text { color: var(--white); font-weight: 700; font-size: 32px; letter-spacing: 1px; }

  .subtitle {
    position: absolute; left: 0; top: 140px; width: 750px; text-align: center;
    font-weight: 900; font-size: 44px; letter-spacing: 1px;
  }

  .title { position: absolute; left: 40px; top: 215px; width: 680px; font-weight: 900; line-height: 1; }
  .title__line { display: block; white-space: nowrap; margin-bottom: 18px; }
  .title__xl { font-size: 150px; letter-spacing: -4px; }
  .title__l { font-size: 120px; letter-spacing: -2px; }
  .title__m { font-size: 96px; }

  .burst { position: absolute; left: 560px; top: 640px; }

  .bottom-panel { position: absolute; left: 0; top: 960px; }

  .reader-badge {
    position: absolute; left: 28px; top: 1000px; width: 178px; height: 178px; border-radius: 50%;
    background: var(--green-main);
    display: flex; flex-direction: column; align-items: center; justify-content: center;
    color: var(--white); font-weight: 900; line-height: 1.05;
  }
  .reader-badge__big { font-size: 40px; }
  .reader-badge__small { font-size: 20px; margin-top: 6px; }

  .gift { position: absolute; left: 228px; top: 1035px; width: 510px; font-weight: 900; }
  .gift__event { font-size: 19px; font-weight: 700; white-space: nowrap; }
  .gift__talk { font-size: 35px; margin-top: 8px; white-space: nowrap; letter-spacing: -1px; }
  .gift__offer { font-size: 32px; margin-top: 6px; white-space: nowrap; }
</style>
</head>
<body>
<main class="cover">
  <div class="cover__backdrop" role="img" aria-label="緑から黄緑へ広がる多角形模様の背景"></div>

  <div class="lead-band"><p class="lead-band__text">パート主婦が口ぐせを変えて</p></div>

  <p class="subtitle">手作り雑貨の通販サイトを始めて</p>

  <h1 class="title">
    <span class="title__line"><span class="title__xl">2年</span><span class="title__m">で月商</span></span>
    <span class="title__line"><span class="title__l">200万円に</span></span>
    <span class="title__line"><span class="title__m">育てた</span><span class="title__l">道のり</span></span>
  </h1>

  <svg class="burst" width="90" height="90" viewBox="0 0 90 90" aria-hidden="true">
    <g stroke="var(--accent)" stroke-width="9" stroke-linecap="round">
      <line x1="12" y1="40" x2="30" y2="8"/>
      <line x1="34" y1="58" x2="70" y2="34"/>
      <line x1="40" y1="82" x2="80" y2="76"/>
    </g>
  </svg>

  <svg class="bottom-panel" width="750" height="240" viewBox="0 0 750 240" aria-hidden="true">
    <path d="M0 40 Q375 0 750 40 L750 240 L0 240 Z" fill="var(--white)"/>
  </svg>

  <div class="reader-badge">
    <span class="reader-badge__big">読者</span>
    <span class="reader-badge__big">限定</span>
    <span class="reader-badge__small">プレゼント</span>
  </div>

  <div class="gift">
    <p class="gift__event">トークイベント プロジェクト・サンセットベルで登壇した</p>
    <p class="gift__talk">「ティーカップで夢を叶える」</p>
    <p class="gift__offer">トーク内容の動画をプレゼント!</p>
  </div>
</main>
</body>
</html>
```